I own a self service Laundromat. From time to time our machines break or take the customers money. I would like to design a post card that I can send the customer that had trouble with one of the machines along with the return of their money. Maybe on one side of the card say OOPS! with a picture of a clothes washer or clothes dryer. On the other side some text that says we are sorry for the trouble at your last visit. Please see attached return of money and we would love to have you back and satisfied. Thank you again for visiting The Suds Corner. I currently don't have a logo so be as creative as you like.

```html
<!DOCTYPE html>
<html lang="en">
<head>
<meta charset="utf-8">
<title>The Suds Corner – Apology Postcard</title>
<link href="https://fonts.googleapis.com/css2?family=Anton&family=Oswald:wght@500;700&family=Lato:wght@400;700&display=swap" rel="stylesheet">
<style>
  :root{
    --pink:#e8547f;
    --pink-light:#f28fac;
    --ink:#262626;
    --black:#1c1c1c;
    --paper:#ffffff;
    --bg:#ececec;
    --grey-light:#d7dadd;
    --line:#bfbfbf;
  }
  *{margin:0;padding:0;box-sizing:border-box}
  html,body{width:900px;height:1200px;overflow:hidden;background:var(--bg)}
  body{position:relative;font-family:"Lato",Arial,sans-serif;color:var(--ink)}

  .card{position:absolute;left:30px;width:840px;background:var(--paper);overflow:hidden;box-shadow:0 2px 6px rgba(0,0,0,.15)}
  .card--front{top:30px;height:570px}
  .card--back{top:620px;height:550px}
  .card svg.shapes{position:absolute;inset:0;width:100%;height:100%}

  /* front */
  .front-title{position:absolute;top:22px;left:0;width:100%;text-align:center;font-family:"Oswald",sans-serif;font-weight:700;font-size:44px;letter-spacing:1px;color:var(--ink)}
  .oops{position:absolute;left:28px;top:222px;font-family:"Anton",sans-serif;font-size:100px;line-height:1;color:var(--pink);-webkit-text-stroke:3px var(--black);letter-spacing:2px;white-space:nowrap;z-index:2}
  .photo-circle{position:absolute;border-radius:50%;border:6px solid var(--paper);box-shadow:0 0 0 3px var(--grey-light)}
  .photo-circle--customer{left:420px;top:335px;width:170px;height:170px;background:radial-gradient(circle at 45% 40%,#c9cdd1,#7d848a)}
  .photo-circle--drum{left:575px;top:385px;width:155px;height:155px;background:radial-gradient(circle at 50% 50%,#f5a3c0,#6fa7d6 45%,#3a3f45 80%)}

  /* back */
  .brand{position:absolute;left:26px;top:34px;font-family:"Oswald",sans-serif;font-weight:700;color:var(--paper);line-height:1}
  .brand span{display:block;font-size:30px;letter-spacing:1px}
  .brand span + span{font-size:48px;margin-top:4px}
  .photo-circle--folding{left:250px;top:14px;width:170px;height:170px;background:radial-gradient(circle at 50% 45%,#e4e6e8,#9da3a8)}
  .message{position:absolute;left:60px;top:235px;width:340px}
  .message h2{font-family:"Oswald",sans-serif;font-weight:700;font-size:46px;line-height:1;color:var(--pink)}
  .message h3{font-family:"Oswald",sans-serif;font-weight:500;font-size:17px;color:var(--ink);margin-top:6px;letter-spacing:.3px;white-space:nowrap}
  .message p{font-size:16px;line-height:1.45;margin-top:22px;color:#444;text-align:justify}
  .message p.thanks{margin-top:10px;font-size:19px;color:var(--ink);text-align:left}
  .message strong{display:block;color:var(--pink);font-weight:700}
  .stamp{position:absolute;right:60px;top:45px;width:72px;height:82px;border:2px solid #555}
  .address{position:absolute;left:490px;top:280px;width:290px}
  .address i{display:block;height:1px;background:var(--line);margin-bottom:48px}
</style>
</head>
<body>

<section class="card card--front">
  <svg class="shapes" viewBox="0 0 840 570" aria-hidden="true">
    <defs>
      <linearGradient id="laundromat" x1="0" y1="0" x2="1" y2="1">
        <stop offset="0" stop-color="#e9ebed"/>
        <stop offset=".55" stop-color="#a9afb4"/>
        <stop offset="1" stop-color="#5f666c"/>
      </linearGradient>
    </defs>
    <rect x="0" y="95" width="840" height="400" fill="url(#laundromat)" role="img" aria-label="Row of front-loading washing machines in a laundromat"/>
    <path d="M0 95 H840 V160 C620 95 360 95 0 150 Z" fill="var(--paper)"/>
    <path d="M0 150 C360 95 620 95 840 160 V175 C620 112 360 112 0 166 Z" fill="var(--pink)"/>
    <path d="M0 80 C300 120 600 60 840 95 V105 C600 72 300 132 0 92 Z" fill="var(--pink)"/>
    <path d="M0 380 C200 420 420 470 840 440 V570 H0 Z" fill="var(--black)"/>
    <path d="M0 360 C200 400 420 450 840 420 V440 C420 470 200 420 0 380 Z" fill="var(--pink)"/>
    <path d="M0 520 C300 560 560 540 840 500 V570 H0 Z" fill="var(--pink)"/>
  </svg>
  <h1 class="front-title">THE SUDS CORNER</h1>
  <div class="oops">OOPS !!</div>
  <div class="photo-circle photo-circle--customer" role="img" aria-label="Frustrated customer beside a washing machine"></div>
  <div class="photo-circle photo-circle--drum" role="img" aria-label="Colourful laundry spinning inside a washer drum"></div>
</section>

<section class="card card--back">
  <svg class="shapes" viewBox="0 0 840 550" aria-hidden="true">
    <path d="M0 0 H300 C280 60 300 130 250 180 C170 200 80 190 0 210 Z" fill="var(--black)"/>
    <path d="M0 210 C80 190 170 200 250 180 C300 130 280 60 300 0 H312 C292 66 312 140 258 192 C170 212 80 202 0 222 Z" fill="var(--pink)"/>
    <path d="M0 222 C40 300 30 420 0 550 H14 C44 420 54 300 12 220 Z" fill="var(--pink)"/>
    <path d="M0 0 H840 V10 H0 Z" fill="var(--pink-light)"/>
    <line x1="455" y1="190" x2="455" y2="500" stroke="var(--line)" stroke-width="1.5"/>
  </svg>
  <div class="brand"><span>THE SUDS</span><span>CORNER</span></div>
  <div class="photo-circle photo-circle--folding" role="img" aria-label="Smiling customer holding a basket of fresh laundry"></div>
  <div class="message">
    <h2>WE ARE SORRY</h2>
    <h3>FOR THE TROUBLE AT YOUR LAST VISIT</h3>
    <p>Please see attached return of money and we would love to have you back and satisfied.</p>
    <p class="thanks">Thank you again for visiting <strong>The Suds Corner.</strong></p>
  </div>
  <div class="stamp"></div>
  <div class="address"><i></i><i></i><i></i><i></i></div>
</section>

</body>
</html>
```